Company or website name
- Dr. Renaud Vasquelle
- Links to the website
- Retired doctor; professional speaker, Life coach, author, healthcare consultant
- Other Facts

```html
<!DOCTYPE html>
<html lang="en">
<head>
<meta charset="utf-8">
<title>Dr. Renaud Vasquelle</title>
<link rel="stylesheet" href="https://fonts.googleapis.com/css2?family=Arimo:ital,wght@0,400;0,700;1,400&family=Tinos:wght@400;700&display=swap">
<style>
  :root {
    --page-blue: #4d73ff;
    --ink: #111111;
    --muted: #555555;
    --teal: #1e5e58;
    --accent-teal: #3bb8c2;
    --nav-black: #000000;
    --nav-active: #2b2b2b;
    --panel-grey: #e3e3e3;
    --rule-grey: #9a9a9a;
    --link-blue: #2121c9;
    --white: #ffffff;
    --footer-ink: #1d2b6b;
  }
  * { box-sizing: border-box; margin: 0; padding: 0; }
  html, body { width: 1032px; height: 1200px; overflow: hidden; }
  body {
    background: var(--page-blue);
    font-family: "Arimo", Arial, sans-serif;
    color: var(--ink);
    position: relative;
  }
  .brand {
    position: absolute; left: 166px; top: 72px;
    display: flex; align-items: center; gap: 12px;
  }
  .brand-mark { width: 20px; height: 20px; background: var(--white); }
  .brand-name {
    font-family: "Tinos", "Times New Roman", serif;
    font-size: 43px; color: var(--white); font-weight: 400; line-height: 1;
  }
  .hotline { position: absolute; left: 680px; top: 33px; color: var(--white); }
  .hotline-label { font-size: 12.5px; letter-spacing: 0.2px; }
  .hotline-number { font-size: 21.5px; letter-spacing: 1px; margin-top: 6px; }

  .site { position: absolute; left: 150px; top: 163px; width: 740px; }
  .main-nav {
    height: 30px; background: var(--nav-black);
    border-top: 2px solid var(--accent-teal);
    display: flex; align-items: stretch;
  }
  .main-nav a {
    color: #cfcfcf; text-decoration: none; font-size: 10.5px; letter-spacing: 0.9px;
    display: flex; align-items: center; white-space: nowrap; margin-right: 40px;
  }
  .main-nav a.active {
    background: var(--nav-active); color: var(--accent-teal);
    width: 154px; padding-left: 9px; margin-right: 34px;
  }

  .intro {
    background: var(--white); height: 131px; padding: 35px 31px 0;
    font-size: 11.3px; line-height: 23px; letter-spacing: 0.9px; text-align: justify;
  }
  .quote-band {
    background: var(--nav-black); height: 92px;
    display: flex; align-items: center; justify-content: center;
    color: #e6e6e6; font-style: italic; font-size: 8.5px; letter-spacing: 1px;
    text-transform: uppercase; padding-bottom: 6px;
  }
  .content {
    background: var(--panel-grey); height: 722px; position: relative;
    border-bottom: 2px solid var(--accent-teal);
  }
  .section-title {
    font-family: "Tinos", "Times New Roman", serif;
    color: var(--teal); font-size: 23px; font-weight: 400; line-height: 1;
  }
  .wisdom { position: absolute; left: 31px; top: 38px; width: 400px; }
  .wisdom .section-title { margin-bottom: 12px; }
  .tip { margin-bottom: 11px; }
  .tip-title {
    font-family: "Tinos", "Times New Roman", serif; font-size: 12.5px; line-height: 23px;
    text-align: justify; letter-spacing: 0.6px;
  }
  .tip-text {
    font-size: 11px; color: var(--muted); line-height: 23px; letter-spacing: 0.75px; text-align: justify;
  }
  .more-link { display: inline-block; margin-top: 16px; font-size: 10.5px; color: var(--link-blue); }

  .column-rule { position: absolute; left: 463px; top: 25px; width: 1px; height: 453px; background: var(--rule-grey); }
  .sidebar { position: absolute; left: 463px; top: 0; width: 246px; }
  .side-block { padding-left: 31px; }
  .side-menu { padding-top: 38px; }
  .side-menu .section-title { margin-bottom: 12px; }
  .side-menu ul { list-style: none; }
  .side-menu a { font-size: 11px; line-height: 23px; color: var(--link-blue); letter-spacing: 0.6px; }
  .side-rule { height: 1px; background: var(--rule-grey); }
  .side-rule.top { margin-top: 10px; }
  .about { padding-top: 14px; }
  .portrait {
    display: block; width: 123px; height: 145px; margin: 24px 0 0 45px;
    border: 3px solid var(--white);
    background: linear-gradient(180deg, #2f3b86 0%, #4a4f8c 45%, #2a2a35 100%);
  }
  .about-quote {
    font-size: 11px; line-height: 23px; letter-spacing: 0.9px; text-align: justify;
    margin-top: 14px; width: 215px;
  }
  .about-quote .nowrap { white-space: nowrap; }
  .side-rule.bottom { margin-top: 14px; }

  .footer {
    position: absolute; left: 150px; top: 1160px; width: 740px; height: 24px;
    display: flex; align-items: center;
  }
  .social { display: flex; gap: 24px; padding-left: 6px; }
  .social span { width: 16px; height: 16px; border-radius: 50%; background: var(--footer-ink); display: block; }
  .copyright { margin-left: auto; font-size: 9.5px; letter-spacing: 0.8px; color: var(--footer-ink); }
</style>
</head>
<body>
  <header>
    <div class="brand">
      <span class="brand-mark"></span>
      <span class="brand-name">Renaud Vasquelle</span>
    </div>
    <div class="hotline">
      <div class="hotline-label">TALK TO THE EXPERT NOW!</div>
      <div class="hotline-number">(555) 014-2738</div>
    </div>
  </header>

  <div class="site">
    <nav class="main-nav">
      <a class="active" href="#">ABOUT YOUR SPEAKER</a>
      <a href="#">THE 60-SECOND SPARK</a>
      <a href="#">CONTACT US</a>
    </nav>

    <section class="intro">
      The information found on this website is intended to inspire you to achieve your full potential. There are a variety of resources including the 60-Second Spark, the Plain Wisdom Series, Designing Your Best Life, and many other great resources to help make every day a terrific day!
    </section>

    <section class="quote-band">"If you are successful, you will win some false friends and some true enemies; succeed anyway.."</section>

    <main class="content">
      <article class="wisdom">
        <h2 class="section-title">WORDS OF WISDOM</h2>
        <div class="tip">
          <p class="tip-title">Pour your heart into whatever you do</p>
          <p class="tip-text">Having passion for what you do is the ultimate key to being successful at it. Halfhearted efforts usually show through as mediocre effort.</p>
        </div>
        <div class="tip">
          <p class="tip-title">Believe that what you do matters and will make a difference in people's lives.</p>
          <p class="tip-text">You don't have to save the world in one stroke, but you can make a difference one person at a time.</p>
        </div>
        <div class="tip">
          <p class="tip-title">Do more than you are being compensated to do.</p>
          <p class="tip-text">Reaching excellence is about doing what you do anyway. That quality of going the extra mile "just because" is what will set you apart.</p>
        </div>
        <div class="tip">
          <p class="tip-title">After you've done more than you are being compensated for, do it again and again.</p>
          <p class="tip-text">Raise the bar continually. Giving more than you get does come back to you.</p>
        </div>
        <a class="more-link" href="#">Give me more..</a>
      </article>

      <div class="column-rule"></div>

      <aside class="sidebar">
        <div class="side-block side-menu">
          <h2 class="section-title">MENU</h2>
          <ul>
            <li><a href="#">Words of Wisdom</a></li>
            <li><a href="#">Available Seminar Topics</a></li>
            <li><a href="#">Plain Wisdom Series</a></li>
            <li><a href="#">Videos</a></li>
            <li><a href="#">Designing Your Best Life</a></li>
            <li><a href="#">About Your Speaker</a></li>
            <li><a href="#">Want Coaching?</a></li>
            <li><a href="#">Booking Renaud</a></li>
            <li><a href="#">Contact Us</a></li>
          </ul>
        </div>
        <div class="side-rule top"></div>
        <div class="side-block about">
          <h2 class="section-title">ABOUT</h2>
          <div class="portrait" role="img" aria-label="Portrait photo of Dr. Renaud Vasquelle"></div>
          <p class="about-quote">"I hereby pledge my life to my greatest expression of love and service for the benefit of all humanity. I accomplish this by helping people tap into their potential, using the written and spoken word; empowering ordinary people into exceptional <span class="nowrap">life-fulfilled</span> individuals"</p>
        </div>
        <div class="side-rule bottom"></div>
      </aside>
    </main>
  </div>

  <footer class="footer">
    <div class="social" aria-label="Social links">
      <span></span><span></span><span></span>
    </div>
    <p class="copyright">© Copyright 2013 - Dr. Renaud A. Vasquelle. All rights reserved.</p>
  </footer>
</body>
</html>
```